Wordpress Template für Weinkommunikation
Zielgruppe
Kunden und potentielle Kunden, die sich über meine Dienstleistungen und mich informieren wollen.
Meine Arbeitsschwerpunkte sind Kommunikation, PR und Events im Weinbereich.
Meine persönlichen Wein-Schwerpunktländer sind Spanien und Portugal. Die Kunden sind von dort, meine Arbeit ist in Deutschland.
Aufgabenstellung
Ich möchte meine bestehende Website endlich mal richtig gestalten lassen.
- Startseite soll statisch sein.
- Weitere Seiten sollen auch statisch möglich sein.
- 2- oder 3-spaltig
- Template muss Widget-fähig sein
- Möglichkeit der Zweisprachigkeit

```html
<!DOCTYPE html>
<html lang="de">
<head>
<meta charset="utf-8">
<title>Rebe &amp; Rat – Weinkommunikation</title>
<link rel="stylesheet" href="https://fonts.googleapis.com/css2?family=Arimo:wght@400;700&family=Source+Sans+3:wght@400;600;700&display=swap">
<style>
:root{
  --brown-dark:#3f1d0b;
  --brown:#5a2a12;
  --brown-text:#3b1a08;
  --wine:#9b0d0d;
  --orange:#e79a1f;
  --gold-line:#e2c58f;
  --cream:#fbf6ea;
  --cream-deep:#f3e7cc;
  --box-border:#e0c48e;
  --outer:#d9c3a4;
  --nav-text:#f4e6cf;
  --link:#8a5a2a;
}
*{margin:0;padding:0;box-sizing:border-box}
html,body{width:1187px;height:1200px;overflow:hidden}
body{
  position:relative;
  background:linear-gradient(90deg,#c8a983 0,#e9dcc6 4%,#f4ece0 50%,#e9dcc6 96%,#c8a983 100%);
  font-family:"Arimo",Arial,sans-serif;
  color:var(--brown-text);
}
.page{position:absolute;left:51px;top:0;width:1089px;height:1200px;background:var(--cream)}
.site-header{position:absolute;left:0;top:0;width:100%;height:117px;background:#fff}
.brand{position:absolute;left:29px;top:24px;display:flex;align-items:center;gap:14px;
  font-family:"Source Sans 3",sans-serif;font-weight:700;font-size:40px;color:var(--brown-dark);line-height:1}
.brand-mark{width:54px;height:54px;background:var(--wine)}
.brand small{font-size:40px;font-weight:700}

.main-nav{position:absolute;left:0;top:117px;width:100%;height:42px;background:linear-gradient(#5b2c13,#3c1b0a)}
.main-nav ul{list-style:none;display:flex;position:absolute;left:30px;top:11px;
  font-family:"Source Sans 3",sans-serif;font-size:15px;color:var(--nav-text)}
.main-nav li{padding:0 10px;border-left:1px solid var(--orange);line-height:19px}
.main-nav li:first-child{border-left:0;padding-left:0}
.search{position:absolute;left:951px;top:8px;display:flex;align-items:center;gap:6px}
.search span.field{width:106px;height:24px;background:#f6ecd2;border:1px solid #c9a46b;
  font-size:12px;padding:4px 5px;color:var(--brown-text)}
.search span.go{color:var(--nav-text);font-size:13px;font-family:"Source Sans 3",sans-serif}

.hero{position:absolute;left:0;top:159px;width:100%;height:204px;overflow:hidden;
  background:linear-gradient(100deg,#8a4e22 0,#c58a4c 25%,#f0d9b5 45%,#7a5236 60%,#2b1a10 75%,#e9d6c0 90%,#5b3a28 100%)}
.hero-label{position:absolute;left:0;top:91px;width:470px;height:83px;background:rgba(40,20,8,.85)}
.hero-title{position:absolute;left:31px;top:16px;font-family:"Source Sans 3",sans-serif;font-weight:600;font-size:21px;color:#fff}
.hero-sub{position:absolute;left:99px;top:46px;font-family:"Source Sans 3",sans-serif;font-style:italic;font-weight:600;font-size:19px;color:var(--orange)}
.slides{position:absolute;left:842px;top:152px;display:flex;gap:1px;list-style:none}
.slides li{width:38px;height:36px;background:rgba(90,45,20,.85);color:#e6d3bd;
  font-family:"Source Sans 3",sans-serif;font-size:20px;text-align:center;line-height:36px}
.slides li.active{background:#3a1a08;height:44px;margin-top:-6px;width:44px;line-height:50px;color:#fff}

.content{position:absolute;left:0;top:363px;width:100%;height:744px;
  background:linear-gradient(var(--cream-deep),var(--cream) 20px)}
.welcome-title{position:absolute;left:59px;top:64px;font-size:14px;font-weight:700;color:var(--wine)}
.portrait{position:absolute;left:59px;top:91px;width:143px;height:169px;border:1px solid #cdb894;
  background:linear-gradient(#dfe5ea,#9aa4ad 50%,#2a2a2e)}
.intro{position:absolute;left:224px;top:91px;width:400px;font-size:12.6px;font-weight:700;line-height:15px}
.body-text{position:absolute;left:59px;top:282px;width:570px;font-size:11.6px;line-height:14.5px}
.body-text p{margin-bottom:14px}
.body-text .cta{color:var(--wine)}
.divider{position:absolute;left:59px;top:526px;width:570px;height:1px;background:var(--gold-line)}
.news-image{position:absolute;left:59px;top:554px;width:148px;height:118px;border:1px solid #cdb894;
  background:linear-gradient(#fff,#e7e4e4)}
.news{position:absolute;left:224px;top:554px}
.news h3{font-size:13px;font-weight:700;margin-bottom:14px}
.news h3 span{font-weight:400}
.news ul{list-style:none;font-size:12px;line-height:16.2px}
.news li{padding-left:23px;position:relative}
.news li::before{content:"";position:absolute;left:0;top:4px;width:8px;height:8px;background:#c7a775}

.box{position:absolute;left:674px;width:385px;border:1px solid var(--box-border);
  background:linear-gradient(#f8ecd0,#fffaf0 40%);padding:10px 20px}
.box h4{font-size:13px;font-weight:700;color:var(--brown-text)}
.blog{top:58px;height:143px}
.blog p{font-size:12px;margin-top:2px}
.blog-photos{position:absolute;left:20px;top:58px;width:207px;height:70px;background:linear-gradient(90deg,#8a9d6a,#5f7a42,#b9c8a1,#6e8a4f)}
.feed{position:absolute;right:12px;top:70px;width:58px;height:58px;border-radius:10px;background:linear-gradient(#f7a244,#e1640b)}
.book{top:227px;height:170px}
.book-cover{position:absolute;left:20px;top:34px;width:61px;height:123px;background:linear-gradient(#f08a12 70%,#fff 70%)}
.book-text{position:absolute;left:95px;top:34px;width:270px;font-size:12px;line-height:15px}
.book-text strong{display:block;font-size:13px;margin-bottom:2px}
.book .more{position:absolute;right:28px;bottom:12px;font-size:12px;font-weight:700;color:var(--wine)}
.partner-badge{position:absolute;left:679px;top:421px;width:382px;height:78px;border-radius:8px;
  background:linear-gradient(#fdfdfd,#d9d9d9);border:1px solid #c8c8c8}
.newsletter{left:679px;top:528px;width:385px;height:109px}
.newsletter p{position:absolute;left:18px;top:40px;width:210px;font-size:12px;line-height:14px}
.newsletter .field{position:absolute;left:228px;top:45px;width:142px;height:24px;background:#efe3c6;border:1px solid #d6bf90}
.newsletter .send{position:absolute;right:18px;top:80px;font-size:12px;font-weight:700;color:var(--wine)}

.site-footer{position:absolute;left:0;top:1107px;width:100%;height:61px;background:var(--cream)}
.footer-links{position:absolute;left:69px;top:31px;font-family:"Source Sans 3",sans-serif;font-size:13px;color:var(--link)}
.partner-name{position:absolute;left:933px;top:17px;font-family:"Source Sans 3",sans-serif;font-weight:700;font-size:19px;color:var(--wine)}
.bottom-band{position:absolute;left:0;top:1168px;width:100%;height:32px;background:linear-gradient(#4a230d,#2e1406)}
</style>
</head>
<body>
<div class="page">
  <header class="site-header">
    <div class="brand"><span class="brand-mark"></span><span>Rebe &amp; Rat · Jan K. Brede</span></div>
  </header>

  <nav class="main-nav">
    <ul>
      <li>Home</li><li>Wer</li><li>Referenzen</li><li>Buchtipps</li><li>Wein-News</li><li>Wein-Glossar</li><li>Links</li><li>Kontakt</li><li>Blog</li>
    </ul>
    <div class="search"><span class="field">Suche</span><span class="go">go</span></div>
  </nav>

  <section class="hero" role="img" aria-label="Foto liegender Weinflaschen im Regal">
    <div class="hero-label">
      <div class="hero-title">Weinkommunikation &amp; Markenbildung</div>
      <div class="hero-sub">Full Service Beratung vom Wein-Profi</div>
    </div>
    <ol class="slides"><li>1</li><li>2</li><li>3</li><li class="active">4</li><li>5</li><li>6</li></ol>
  </section>

  <main class="content">
    <h2 class="welcome-title">Willkommen bei Rebe &amp; Rat</h2>
    <div class="portrait" role="img" aria-label="Porträtfoto des Weinberaters"></div>
    <p class="intro">Mit Rebe &amp; Rat möchte ich Ihnen vor allem mein Wissen über Wein - insbesondere der Iberischen Halbinsel - über die Weinbau-Länder, die unterschiedlichen Regionen, die abwechslungsreichen Landschaften, die unzähligen Kellereien, die Winzerpersönlichkeiten, aber auch meine ganz persönlichen Eindrücke und Erlebnisse zur Kultur, zur Gastronomie, zu den Menschen und zum Leben in Spanien, Portugal, der Weinwelt und zum Thema Genuss allgemein zugänglich machen.</p>
    <div class="body-text">
      <p>Durch die langjährige Erfahrung im internationalen Weingrosshandel und der Weinszene sind die Bereiche Kommunikation, PR und Marketing, sowie die Sortiments- und Einkaufsberatung, neben den Schulungen ein wichtiger Bestandteil des Angebotes.<br>Speziell im institutionellen Bereich biete ich Verbänden, Regionen und Ländern die Möglichkeit, sich über den deutschen Weinmarkt kundig zu machen, zu eruieren wo und wie sie ihre Produkte am sinnvollsten anbieten können. Hierzu gehört auch die Kommunikations- und Pressearbeit, sowie die Konzeption, Planung und Durchführung von Veranstaltungen.</p>
      <p>In Partnerschaft mit einer Vielzahl von Sommeliers, Weinprofis und anderen Freiberuflern können wir Ihnen darüber hinaus ein breites Spektrum an Leistungen rund um das Thema Wein und Genuss anbieten. Das garantiert Ihnen massgeschneiderte Weinkompetenz ganz nach Ihrem Geschmack und Ihren Wünschen!</p>
      <p class="cta">Sprechen Sie uns einfach an. Wir sind für Sie da!</p>
    </div>
    <div class="divider"></div>
    <div class="news-image" role="img" aria-label="Foto von Weingläsern"></div>
    <section class="news">
      <h3>Aktuelle Wein-News <span>(by Traubenforum.de)</span></h3>
      <ul>
        <li>Winzer relativ zufrieden</li>
        <li>Erste-Lage-Spätlesen im Rampenlicht</li>
        <li>Neue Sommelier-Ausbildung</li>
        <li>Ernte 2010 in Südtirol: Wenig, aber sehr gut</li>
        <li>Betrüger verurteilt</li>
        <li>Majestät kommt von der Ahr</li>
        <li>Weinköniginnen-Halbfinale beendet</li>
        <li>Neue Deutsche Weinkönigin steht vor der Wahl</li>
      </ul>
    </section>

    <aside class="box blog">
      <h4>blog.rebe-rat.de - mein Blog mit Infos, News</h4>
      <p>Aus der Weinwelt von Rebe &amp; Rat ...</p>
      <div class="blog-photos" role="img" aria-label="Fotos von Weinbergen"></div>
      <div class="feed" aria-label="Feed abonnieren"></div>
    </aside>
    <aside class="box book">
      <h4>Buchtipp des Monats</h4>
      <div class="book-cover" role="img" aria-label="Buchcover Weinführer 2010"></div>
      <div class="book-text"><strong>Lorenz Adlers kleiner genialer Weinführer 2010</strong>Die Neuauflage von Lorenz Adlers kleinem genialen Weinführer. Er liefert Tipps für den Weineinkauf und einige ungewöhnliche Auszeichnungen.</div>
      <span class="more">mehr Bücher</span>
    </aside>
    <div class="partner-badge" role="img" aria-label="Partnerbanner"></div>
    <aside class="box newsletter">
      <h4>Newsletter</h4>
      <p><strong>Melden Sie sich an</strong> und bleiben immer aktuell informiert über Interessantes aud der Weinwelt</p>
      <span class="field"></span>
      <span class="send">Jetzt anmelden</span>
    </aside>
  </main>

  <footer class="site-footer">
    <div class="footer-links">Kontakt | Impressum | Blog | Wein-Glossar | Adresse</div>
    <div class="partner-name">Traubenforum.de</div>
  </footer>
  <div class="bottom-band"></div>
</div>
</body>
</html>
```